Business Card for innovative, tech/consultant company

We are specializing in bringing together Efficiency methodology and Technology for our Business customers. We would like an astonishing business Card that matches this idea.

Target Market(s)

Businesses of medium size or more

Industry/Entity Type

Business Consultant

Contact Information for Business Card

Name, Title, personal email, www, address, phone

Font styles to use
Sans Serif

Colors
3277b5

Requirements
Must have
• - innovative, efficient design
• - good readable
• - Colors must match our logo (blue and grey)
• - the attached font (is licensed by our Company) must be used (Syntax LT)
Should not have
• overloaded

```html
<!DOCTYPE html>
<html lang="en">
<head>
<meta charset="utf-8">
<title>Lumora Business Card</title>
<link rel="stylesheet" href="https://fonts.googleapis.com/css2?family=Nunito+Sans:wght@400;700&display=swap">
<style>
  :root {
    --brand-blue: #1673b8;
    --text-grey: #6f7073;
    --logo-grey: #7a7b7e;
    --bar-grey: #808184;
    --card-white: #ffffff;
    --page-bg: #ebe8e5;
  }
  * { margin: 0; padding: 0; box-sizing: border-box; }
  html, body {
    width: 1200px;
    height: 1000px;
    overflow: hidden;
    background: var(--page-bg);
    font-family: "Nunito Sans", sans-serif;
  }
  .business-card {
    position: absolute;
    left: 120px;
    top: 212px;
    width: 960px;
    height: 575px;
    background: var(--card-white);
    border-radius: 32px;
    overflow: hidden;
    box-shadow: 0 6px 18px rgba(0, 0, 0, 0.12);
  }
  .brand-name {
    position: absolute;
    left: 52px;
    top: 46px;
    font-size: 140px;
    font-weight: 400;
    line-height: 1;
    letter-spacing: -2px;
    color: var(--logo-grey);
  }
  .name-tab {
    position: absolute;
    left: 0;
    top: 299px;
    width: 14px;
    height: 82px;
    background: var(--brand-blue);
    border-radius: 0 7px 7px 0;
  }
  .person {
    position: absolute;
    left: 48px;
    top: 306px;
  }
  .person-name {
    font-size: 35px;
    font-weight: 700;
    color: var(--brand-blue);
    line-height: 1.1;
  }
  .person-title {
    font-size: 24px;
    font-weight: 400;
    color: var(--text-grey);
    line-height: 1.3;
  }
  .contact-row {
    position: absolute;
    left: 48px;
    top: 436px;
    right: 30px;
    display: flex;
    font-size: 24px;
    color: var(--text-grey);
    line-height: 36px;
  }
  .contact-group { display: flex; flex-direction: column; }
  .contact-address { width: 283px; }
  .divider {
    width: 3px;
    height: 60px;
    background: var(--brand-blue);
    margin-top: 4px;
  }
  .contact-phones { width: 297px; padding-left: 42px; }
  .contact-web { padding-left: 46px; }
  .contact-line { display: flex; align-items: center; gap: 12px; white-space: nowrap; }
  .contact-line svg { width: 22px; height: 22px; flex: none; }
  .bottom-bands {
    position: absolute;
    left: 0;
    bottom: 0;
    width: 100%;
    height: 36px;
  }
  .band { position: absolute; top: 0; height: 100%; }
  .band-left { left: 0; width: 250px; background: var(--bar-grey); }
  .band-center { left: 257px; width: 446px; background: var(--brand-blue); }
  .band-right { left: 709px; right: 0; background: var(--bar-grey); }
</style>
</head>
<body>
  <main class="business-card">
    <p class="brand-name">Lumora</p>

    <span class="name-tab"></span>
    <div class="person">
      <p class="person-name">Daniel Reyes</p>
      <p class="person-title">Owner / Founder</p>
    </div>

    <div class="contact-row">
      <div class="contact-group contact-address">
        <span>42 Harbor Lane,</span>
        <span>Millbrook, 30418</span>
      </div>
      <span class="divider"></span>
      <div class="contact-group contact-phones">
        <span class="contact-line">
          <svg viewBox="0 0 22 22" aria-hidden="true"><rect x="6" y="1.5" width="10" height="19" rx="1.5" fill="none" stroke="#1673b8" stroke-width="2"/><rect x="9.5" y="16.5" width="3" height="1.6" fill="#1673b8"/></svg>
          + 000 000 0000
        </span>
        <span class="contact-line">
          <svg viewBox="0 0 22 22" aria-hidden="true"><path d="M2 8 Q11 1 20 8 L17 10 L15 7 Q11 5 7 7 L5 10 Z" fill="#1673b8"/><path d="M5 11 H17 L19 19 H3 Z" fill="#1673b8"/><circle cx="11" cy="15" r="2.4" fill="#fff"/></svg>
          + 000 000 0000
        </span>
      </div>
      <span class="divider"></span>
      <div class="contact-group contact-web">
        <span class="contact-line">
          <svg viewBox="0 0 22 22" aria-hidden="true"><rect x="1.5" y="5" width="19" height="13" fill="#1673b8"/><path d="M1.5 5 L11 12.5 L20.5 5" fill="none" stroke="#fff" stroke-width="1.6"/></svg>
          info@lumora.co.uk
        </span>
        <span class="contact-line">
          <svg viewBox="0 0 22 22" aria-hidden="true"><rect x="2" y="4" width="18" height="12" fill="none" stroke="#1673b8" stroke-width="2.2"/><rect x="7" y="18" width="8" height="2" fill="#1673b8"/></svg>
          www.lumora.co.uk
        </span>
      </div>
    </div>

    <div class="bottom-bands">
      <span class="band band-left"></span>
      <span class="band band-center"></span>
      <span class="band band-right"></span>
    </div>
  </main>
</body>
</html>
```